Fast Growing Personal Injury Law Firm Needs Business Card Design

We need a business card design for a fast growing personal injury law firm in Florida. Our name is Dorian Halvorsk, P.A. Our practice is comprised of younger attorneys (in their 30s) that employ more modern techniques/tools than our older competition. We would prefer a look that is a modern play on a classic look. Also, we would like to continue using a color scheme that employs navy blue and kelly green (other shades of green could be fine too) as well as our "E" logo.

Industry/Entity Type

Law Firm

```html
<!DOCTYPE html>
<html lang="en">
<head>
<meta charset="utf-8">
<title>Dorian Halvorsk, P.A. — Business Card</title>
<link rel="stylesheet" href="https://fonts.googleapis.com/css2?family=Gelasio:ital,wght@0,400;0,700;1,400&display=swap">
<style>
  :root {
    --navy: #1b3a8a;
    --kelly: #0f9a47;
    --sky: #6cc0ec;
    --lime: #7bbd2a;
    --card-black: #17191b;
    --paper: #fbfbfb;
    --ink: #1d2f6f;
    --stage: #e6e6e4;
  }
  * { margin: 0; padding: 0; box-sizing: border-box; }
  html, body { width: 1200px; height: 768px; overflow: hidden; }
  body {
    background: var(--stage);
    font-family: "Gelasio", Georgia, serif;
    position: relative;
  }
  .card {
    position: absolute;
    top: 234px;
    width: 520px;
    height: 300px;
    overflow: hidden;
    box-shadow: 0 6px 18px rgba(0,0,0,.18);
  }
  /* Back side */
  .card-back {
    left: 50px;
    background: var(--card-black);
    display: flex;
    align-items: center;
    justify-content: center;
    gap: 14px;
  }
  .card-back .mark-square {
    width: 26px; height: 26px;
    background: var(--sky);
    flex: none;
  }
  .card-back .firm-wordmark {
    color: var(--sky);
    font-weight: 700;
    font-size: 26px;
  }
  /* Front side */
  .card-front { left: 630px; background: var(--paper); }
  .front-header {
    position: absolute; left: 22px; top: 22px;
    display: flex; align-items: flex-start; gap: 12px;
  }
  .front-header .mark-square {
    width: 44px; height: 44px; background: var(--navy); flex: none;
  }
  .firm-name {
    color: var(--navy); font-weight: 700; font-size: 27px; line-height: 1;
  }
  .firm-tagline {
    color: var(--kelly); font-weight: 700; font-size: 21px; line-height: 1.1;
    letter-spacing: .5px; margin-top: 2px;
  }
  .attorney {
    position: absolute; left: 22px; top: 90px;
  }
  .attorney-name { color: var(--ink); font-weight: 700; font-size: 16px; }
  .attorney-title { color: var(--ink); font-style: italic; font-size: 12px; }
  .rule-green {
    position: absolute; left: 200px; right: 0; top: 108px;
    height: 1.5px; background: var(--kelly);
  }
  .contacts {
    position: absolute; left: 22px; top: 134px; list-style: none;
  }
  .contacts li {
    display: flex; align-items: center; gap: 8px;
    color: var(--ink); font-size: 13px; line-height: 19px;
  }
  .contacts svg { width: 11px; height: 11px; fill: var(--kelly); flex: none; }
  .rule-green-low {
    position: absolute; left: 0; right: 0; top: 224px;
    height: 1.5px; background: var(--kelly);
  }
  .address-band {
    position: absolute; left: 0; bottom: 28px; width: 380px; height: 24px;
    background: var(--kelly);
    color: #fff; font-size: 11.5px; line-height: 24px; padding-left: 14px;
    white-space: nowrap;
  }
  .footer-square {
    position: absolute; left: 388px; bottom: 22px;
    width: 36px; height: 36px; background: var(--navy);
  }
  .navy-band {
    position: absolute; left: 432px; right: 0; bottom: 28px; height: 24px;
    background: var(--navy);
  }
</style>
</head>
<body>
  <section class="card card-back" aria-label="Card back">
    <span class="mark-square"></span>
    <span class="firm-wordmark">Dorian Halvorsk, P.A.</span>
  </section>

  <section class="card card-front" aria-label="Card front">
    <header class="front-header">
      <span class="mark-square"></span>
      <div>
        <div class="firm-name">Dorian Halvorsk, P.A.</div>
        <div class="firm-tagline">Personal Injury Attorneys</div>
      </div>
    </header>

    <div class="attorney">
      <div class="attorney-name">Dorian Halvorsk</div>
      <div class="attorney-title">Attorney at Law</div>
    </div>
    <div class="rule-green"></div>

    <ul class="contacts">
      <li><svg viewBox="0 0 12 12"><path d="M3 1l2 2-1 1.5c.7 1.5 1.8 2.6 3.5 3.5L9 7l2 2-1.5 2C5 10.5 1.5 7 1 2.5z"/></svg>941 555 0142</li>
      <li><svg viewBox="0 0 12 12"><rect x="3" y="1" width="6" height="3"/><rect x="1" y="4.5" width="10" height="4.5"/><rect x="3" y="8" width="6" height="3"/></svg>941 555 0178</li>
      <li><svg viewBox="0 0 12 12"><path d="M1 2.5h10v7H1z M1.5 3l4.5 3.5L10.5 3" stroke="#fff" stroke-width=".8"/></svg>dorian@halvorsklaw.com</li>
      <li><svg viewBox="0 0 12 12"><circle cx="6" cy="6" r="5"/><path d="M1 6h10M6 1c-2.5 3-2.5 7 0 10M6 1c2.5 3 2.5 7 0 10" stroke="#fff" stroke-width=".7" fill="none"/></svg>www.halvorsklaw.com</li>
    </ul>

    <div class="rule-green-low"></div>
    <div class="address-band">1250 Meridian Parkway Suite 410 Palmetto Grove, Florida 34290</div>
    <span class="footer-square"></span>
    <div class="navy-band"></div>
  </section>
</body>
</html>
```